Business Card for Kinesiologist Practitioner

I need a logo and business card designing for a Kinesiologist Practitioner. I would like the card to be double sided. The look and feel of the logo and graphics should depict natural healing and well being. I would like a modern, fresh and contemporary design with a professional style. I have attached some logos and business cards that I liek from other natural health practitioners. I have also attached some logos that I like and a mock up of the business card style. Please however use your own creative input to change any element as you feel appropriate.

I have used the strap line "Quiet Meadow Care" which I would like underneath the logo. For the logo I like natural objects and possibly with 3 elements in the design as the course I have studied follows a "Lumora " healing concept (mind, body, soul). Maybe a tree or flower with 3 elements and a representation or suggestion of the human body somehow. You will see from the logos i have uploaded

Industry/Entity Type

Business

Contact Information for Business Card

Please see the mock up attached.

Font styles to use
Serif
Sans Serif

Colors
faa54b
acd036
fbee3d
85cae6

Requirements
Must have
• Note the colours are just suggested colours. Please us your own creative licence.

```html
<!DOCTYPE html>
<html lang="en">
<head>
<meta charset="utf-8">
<title>Quiet Meadow Care – Business Card</title>
<link rel="stylesheet" href="https://fonts.googleapis.com/css2?family=Open+Sans:wght@400;600&display=swap">
<style>
  :root {
    --backdrop: #3a3330;
    --card-black: #0b0b0b;
    --card-black-soft: #151515;
    --lime: #acd036;
    --text-white: #f2f2f2;
    --silver: #d6d6d6;
  }
  * { box-sizing: border-box; margin: 0; padding: 0; }
  html, body {
    width: 1200px;
    height: 900px;
    overflow: hidden;
    background: var(--backdrop);
  }
  .canvas {
    position: relative;
    width: 1200px;
    height: 900px;
    display: flex;
    align-items: center;
    justify-content: center;
    gap: 50px;
  }
  .card {
    position: relative;
    width: 525px;
    height: 300px;
    background: radial-gradient(circle at 40% 35%, var(--card-black-soft), var(--card-black) 70%);
    border-radius: 3px;
    box-shadow: 0 10px 30px rgba(0,0,0,0.45);
    overflow: hidden;
  }

  /* Front side */
  .front-brand {
    position: absolute;
    left: 30px;
    top: 0;
    width: 215px;
    height: 100%;
    display: flex;
    align-items: center;
    justify-content: center;
    gap: 10px;
  }
  .brand-dot {
    width: 12px;
    height: 12px;
    border-radius: 50%;
    background: var(--lime);
    flex: none;
  }
  .brand-name {
    font-family: "Open Sans", sans-serif;
    font-weight: 600;
    font-size: 21px;
    line-height: 1.2;
    color: var(--lime);
  }
  .divider {
    position: absolute;
    left: 262px;
    top: 55px;
    width: 1px;
    height: 190px;
    background: linear-gradient(to bottom, transparent, var(--lime) 30%, var(--lime) 70%, transparent);
    opacity: 0.7;
  }
  .contact {
    position: absolute;
    left: 290px;
    top: 62px;
    font-family: "Open Sans", sans-serif;
    color: var(--text-white);
    font-size: 13.5px;
    line-height: 1.3;
  }
  .contact-name {
    font-weight: 600;
    font-size: 16px;
    color: var(--lime);
  }
  .contact-role { margin-bottom: 14px; }
  .contact-address { margin-bottom: 14px; }
  .contact-line {
    display: flex;
    align-items: center;
    gap: 9px;
  }
  .contact-line svg {
    width: 11px;
    height: 11px;
    fill: var(--lime);
    flex: none;
  }

  /* Back side */
  .back-brand {
    position: absolute;
    right: 44px;
    top: 0;
    height: 100%;
    display: flex;
    align-items: center;
    gap: 14px;
  }
  .back-brand-dot {
    width: 14px;
    height: 14px;
    border-radius: 50%;
    background: var(--silver);
    flex: none;
  }
  .back-brand-name {
    font-family: "Open Sans", sans-serif;
    font-weight: 400;
    font-size: 34px;
    line-height: 1;
    color: var(--silver);
  }
</style>
</head>
<body>
<main class="canvas">

  <section class="card card-front">
    <div class="front-brand">
      <span class="brand-dot"></span>
      <span class="brand-name">Quiet Meadow Care</span>
    </div>
    <div class="divider"></div>
    <div class="contact">
      <p class="contact-name">Mara Ellison</p>
      <p class="contact-role">Managing Director</p>
      <p class="contact-address">48, Willow Lane Studios<br>Greenfield, 246810.</p>
      <p class="contact-line">
        <svg viewBox="0 0 24 24"><path d="M6.6 10.8a15.1 15.1 0 0 0 6.6 6.6l2.2-2.2a1 1 0 0 1 1-.25 11.4 11.4 0 0 0 3.6.57 1 1 0 0 1 1 1V20a1 1 0 0 1-1 1A17 17 0 0 1 3 4a1 1 0 0 1 1-1h3.5a1 1 0 0 1 1 1c0 1.25.2 2.45.57 3.57a1 1 0 0 1-.25 1z"/></svg>
        055-246 810 357
      </p>
      <p class="contact-line">
        <svg viewBox="0 0 24 24"><path d="M2 5h20v2l-10 7L2 7z"/><path d="M2 9l10 7 10-7v10H2z"/></svg>
        hello@quietmeadow.com
      </p>
      <p class="contact-line">
        <svg viewBox="0 0 24 24"><circle cx="12" cy="12" r="10"/></svg>
        www.quietmeadowcare.com
      </p>
    </div>
  </section>

  <section class="card card-back">
    <div class="back-brand">
      <span class="back-brand-dot"></span>
      <span class="back-brand-name">Quiet Meadow Care</span>
    </div>
  </section>

</main>
</body>
</html>
```